Book Cover for the book: Walk the Path You Were Given

We are wanting a rebranding of the book cover for the book - Walk the Path You Were Given: How to Hear Your Inner Compass and Uncover Your Calling, Talents and Strength.

We would like to see front, back and spine designs included.

Please stay with the color schemes included in the existing cover (see attached) . We would like to see designs with a snowflake, or hummingbird element included in the design.

Back Cover should include the copy included in the attached file, incorporate all or some of the reviews included in the documents uploaded and image of author.

Please include the authors name: Marisol Thackery on front, spine and back cover of the book

Target Market(s)

Healers, Visionaries

Requirements
Must have
• See Project Description

```html
<!DOCTYPE html>
<html lang="en">
<head>
<meta charset="utf-8">
<title>Walk the Path You Were Given – Book Cover</title>
<link rel="stylesheet" href="https://fonts.googleapis.com/css2?family=Marcellus&family=Goudy+Bookletter+1911&family=Lato:ital,wght@0,400;0,700;0,900;1,400;1,700&family=Pathway+Gothic+One&family=Sorts+Mill+Goudy:ital@1&display=swap">
<style>
  :root {
    --sky-top: #86d2f6;
    --sky-bottom: #b2effd;
    --plum: #a04a9e;
    --ink: #111111;
    --frost: rgba(120, 200, 235, 0.55);
    --bird-green: #7fa36a;
    --bird-rose: #c34c9a;
    --photo-blue: #2f5f9e;
    --photo-gold: #c9a24a;
    --paper: #ffffff;
  }
  * { margin: 0; padding: 0; box-sizing: border-box; }
  html, body { width: 1200px; height: 900px; overflow: hidden; }
  body { background: var(--sky-top); }

  .cover {
    position: relative;
    width: 1200px;
    height: 900px;
    background: linear-gradient(180deg, var(--sky-top) 0%, var(--sky-bottom) 100%);
    overflow: hidden;
    color: var(--ink);
  }

  /* ---------- back cover ---------- */
  .frost-motif {
    position: absolute;
    left: -40px; top: 420px;
    width: 440px; height: 440px;
    border-radius: 50%;
    background: radial-gradient(circle, var(--frost) 0%, rgba(140,210,240,0.25) 50%, rgba(140,210,240,0) 72%);
  }
  .back-title {
    position: absolute;
    left: 30px; top: 44px; width: 520px;
    font-family: "Marcellus", serif;
    font-size: 29px;
    letter-spacing: 0.01em;
    color: var(--plum);
    text-align: center;
    white-space: nowrap;
  }
  .back-rule {
    position: absolute;
    left: 98px; top: 92px;
    width: 382px; height: 1px;
    background: var(--ink);
  }
  .bio {
    position: absolute;
    left: 31px; top: 123px; width: 520px;
    font-family: "Lato", sans-serif;
    font-size: 14.6px;
    line-height: 20px;
  }
  .author-photo {
    float: left;
    width: 106px; height: 95px;
    margin: 0 5px 0 6px;
    background: linear-gradient(135deg, var(--photo-blue) 0%, var(--photo-blue) 40%, var(--photo-gold) 100%);
  }
  .bio-name {
    display: block;
    font-size: 15.5px;
    text-decoration: underline;
    text-underline-offset: 2px;
    line-height: 18px;
    margin-bottom: 2px;
  }
  .bio p + p { margin-top: 20px; }

  .praise-heading {
    position: absolute;
    left: 60px; top: 447px; width: 460px;
    font-family: "Lato", sans-serif;
    font-weight: 900;
    font-size: 17px;
    line-height: 22px;
    text-align: center;
    letter-spacing: 0.02em;
  }
  .review {
    position: absolute;
    left: 31px; width: 517px;
    font-family: "Lato", sans-serif;
    font-style: italic;
    font-size: 12.2px;
    line-height: 16.8px;
  }
  .review-one { top: 513px; }
  .review-two { top: 580px; }
  .review-lead { font-weight: 700; font-size: 13px; }
  .review-by { display: block; text-align: right; font-weight: 700; font-size: 12.6px; margin-top: 1px; }

  .isbn-panel {
    position: absolute;
    left: 351px; top: 755px;
    width: 200px; height: 120px;
    background: var(--paper);
  }

  /* ---------- spine ---------- */
  .spine-title {
    position: absolute;
    left: 577px; top: 30px;
    writing-mode: vertical-rl;
    font-family: "Marcellus", serif;
    font-size: 27px;
    color: var(--plum);
    white-space: nowrap;
    letter-spacing: 0.01em;
  }
  .spine-bird {
    position: absolute;
    left: 578px; top: 535px;
    width: 42px; height: 40px;
    border-radius: 50%;
    background: radial-gradient(circle, var(--bird-rose) 0%, var(--bird-green) 45%, rgba(127,163,106,0) 72%);
  }
  .spine-author {
    position: absolute;
    left: 578px; top: 645px;
    writing-mode: vertical-rl;
    font-family: "Pathway Gothic One", sans-serif;
    font-size: 37px;
    white-space: nowrap;
  }

  /* ---------- front cover ---------- */
  .front-subtitle {
    position: absolute;
    left: 660px; top: 22px; width: 500px;
    font-family: "Goudy Bookletter 1911", serif;
    font-size: 29px;
    line-height: 37px;
    text-align: center;
  }
  .front-title {
    position: absolute;
    left: 700px; top: 160px; width: 460px;
    font-family: "Goudy Bookletter 1911", serif;
    color: var(--plum);
    text-align: center;
    list-style: none;
  }
  .front-title span { display: block; font-size: 92px; line-height: 104px; letter-spacing: 0.14em; }
  .front-title .small { font-size: 60px; letter-spacing: 0.12em; margin-right: 0.35em; }
  .front-title .line { white-space: nowrap; }
  .front-bird {
    position: absolute;
    left: 985px; top: 318px;
    width: 200px; height: 180px;
    border-radius: 50% 40% 50% 45%;
    background: radial-gradient(ellipse at 45% 45%, var(--bird-rose) 0%, var(--bird-green) 40%, rgba(127,163,106,0.35) 60%, rgba(127,163,106,0) 72%);
  }
  .front-author {
    position: absolute;
    left: 660px; top: 755px; width: 500px;
    font-family: "Pathway Gothic One", sans-serif;
    font-size: 64px;
    line-height: 70px;
    text-align: center;
    white-space: nowrap;
  }
  .front-quote {
    position: absolute;
    left: 668px; top: 832px; width: 484px;
    font-family: "Sorts Mill Goudy", serif;
    font-style: italic;
    font-size: 12.2px;
    line-height: 15.5px;
    text-align: center;
  }
</style>
</head>
<body>
<main class="cover">

  <!-- back cover -->
  <div class="frost-motif" role="img" aria-label="Faint pale-blue snowflake motif"></div>
  <h2 class="back-title">WALK THE PATH YOU WERE GIVEN</h2>
  <div class="back-rule"></div>

  <section class="bio">
    <div class="author-photo" role="img" aria-label="Portrait photograph of the author"></div>
    <span class="bio-name">MARISOL THACKERY PHD</span>
    <p><strong><em>Walking the path you were given</em></strong>, (i.e. the process of aligning with your real nature), is what brings success and fulfilment to you. Your alignment with the unique passion that drives you creates an irresistible magnetic force in your energy field that the universe can’t ignore. You become magnetic to better outcomes. And you become able to create the kind of life you desire. Particularly if you are a sensitive person.</p>
    <p>&nbsp;I gained access to my authentic energy and my soul’s highest gifts – after only twelve months, my success rates in healing sessions with people who had been studying spirituality and healing for years were through the roof. They were coming to me for help because I aligned with and started walking the path I was given. And you can align with your highest purpose and your real nature too. Here's to your success!</p>
  </section>

  <h3 class="praise-heading">WHAT PEOPLE ARE SAYING ABOUT<br>WALK THE PATH YOU WERE GIVEN</h3>

  <blockquote class="review review-one">
    Very insightful for sensitive people who feel disconnected from their purpose excellent book! Made me weep but gave me so much perspective on why I feel as I do about myself.
    <span class="review-by">- Delia Brannock</span>
  </blockquote>

  <blockquote class="review review-two">
    <span class="review-lead">A meaningful, heartfelt, communication</span><br>
    A very interesting well written read, holding the attention of the reader and in many areas resonating on a collective and individual level I feel. If you have found this book title you should most definitely read it. Whatever you may be struggling with right now in life, in relationships, reaching for your spiritual needs and self nurturing. This book I feel will help anyone who reads it. Thanks to Marisol + those spiritual communicators that inspire so many.
    <span class="review-by">- Wren.</span>
  </blockquote>

  <div class="isbn-panel"></div>

  <!-- spine -->
  <div class="spine-title">WALK THE PATH YOU WERE GIVEN</div>
  <div class="spine-bird" role="img" aria-label="Small hummingbird illustration"></div>
  <div class="spine-author">Marisol Thackery, PhD</div>

  <!-- front cover -->
  <p class="front-subtitle">How to Hear Your Inner Compass<br>and Uncover Your Calling,<br>Talents and Strength</p>

  <h1 class="front-title">
    <span class="line">WALK</span>
    <span class="line"><span class="small" style="display:inline">THE</span><span style="display:inline">PATH</span></span>
    <span class="line">YOU</span>
    <span class="line">WERE</span>
    <span class="line">GIVEN</span>
  </h1>
  <div class="front-bird" role="img" aria-label="Hummingbird illustration in flight with green wings and magenta throat"></div>

  <p class="front-author">Marisol Thackery, PhD</p>
  <p class="front-quote">This is the best book I've ever read on finding your purpose (and I've read a lot). The author clearly speaks from experience and wisdom and opens you up to understanding yourself on a whole new level. Thank you for writing this book and sharing your wisdom. Truely life changing!</p>

</main>
</body>
</html>
```